App Icon Designs

I am creating an app and I need icons for these categories:
Education
Entertainment
Finance
Games
Health & Fitness
Kids
Lifestyle
Medical
Music
Navigation
News
Photo & Video
Social Networking
Sports
Travel
Utilities
Weather
I would like the icon designs to imitate the style of the included picture. I have also included a picture of the buttons the icons should fit in (75 x 75 pixels). The icons should stick the the simple and flat look.
Please keep all icons 75 x 75 pixels, and NOT 90 x 90 pixels.
Prize increased to $230. Please do your best work. If anyone can successfully imitate the design of the picture included, I will be glad to increase the prize by another $100.

```html
<!DOCTYPE html>
<html lang="en">
<head>
<meta charset="utf-8">
<title>Category Lock Screen</title>
<link rel="stylesheet" href="https://fonts.googleapis.com/css2?family=Open+Sans:wght@400;600&display=swap">
<style>
  :root {
    --page-bg: #ececec;
    --screen-bg: #d6d6d6;
    --status-bg: #111111;
    --status-ink: #e6e6e6;
    --business: #4d6db0;
    --education: #5bbcc4;
    --entertainment: #eebc4c;
    --finance: #23bd9b;
    --games: #dc5b8b;
    --label-ink: #ffffff;
    --unlock-bg: #3a3a3a;
    --track-bg: #1c1c1c;
    --knob-bg: #e4e4e4;
    --knob-ink: #6a6a6a;
    --track-ink: #9a9a9a;
    --icon-tint: rgba(255, 255, 255, 0.28);
  }
  * { box-sizing: border-box; margin: 0; padding: 0; }
  html, body {
    width: 1200px;
    height: 977px;
    overflow: hidden;
    background: var(--page-bg);
    font-family: "Open Sans", Arial, sans-serif;
  }
  .lock-screen {
    position: absolute;
    left: 346px;
    top: 38px;
    width: 508px;
    height: 900px;
    background: var(--screen-bg);
    overflow: hidden;
  }
  .status-bar {
    height: 34px;
    background: var(--status-bg);
    display: flex;
    align-items: center;
    justify-content: space-between;
    padding: 0 12px;
  }
  .status-bar svg { display: block; }
  .category-list {
    list-style: none;
    padding: 14px 12px 0;
    display: flex;
    flex-direction: column;
    gap: 12px;
  }
  .category {
    position: relative;
    height: 122px;
    border-radius: 8px;
    overflow: hidden;
    display: flex;
    align-items: center;
    padding-left: 26px;
    color: var(--label-ink);
  }
  .category--business { background: var(--business); }
  .category--education { background: var(--education); }
  .category--entertainment { background: var(--entertainment); }
  .category--finance { background: var(--finance); }
  .category--games { background: var(--games); }
  .category__sheen {
    position: absolute;
    inset: 0;
    pointer-events: none;
  }
  .category__icon {
    width: 64px;
    height: 64px;
    border-radius: 10px;
    background: var(--icon-tint);
    flex: none;
    margin-top: -30px;
  }
  .category__label {
    font-weight: 600;
    font-size: 24px;
    margin-left: 10px;
    margin-top: 30px;
    letter-spacing: 0.2px;
    position: relative;
  }
  .unlock-panel {
    position: absolute;
    left: 0;
    right: 0;
    bottom: 0;
    height: 180px;
    background: var(--unlock-bg);
    display: flex;
    align-items: center;
    justify-content: center;
  }
  .unlock-track {
    width: 440px;
    height: 96px;
    border-radius: 16px;
    background: var(--track-bg);
    display: flex;
    align-items: center;
    padding: 0 8px;
  }
  .unlock-knob {
    width: 118px;
    height: 80px;
    border-radius: 12px;
    background: var(--knob-bg);
    display: flex;
    align-items: center;
    justify-content: center;
    flex: none;
  }
  .unlock-text {
    flex: 1;
    text-align: center;
    font-size: 34px;
    font-weight: 400;
    color: var(--track-ink);
  }
</style>
</head>
<body>
  <main class="lock-screen">
    <header class="status-bar">
      <svg class="signal" width="22" height="14" viewBox="0 0 22 14" aria-label="Signal">
        <rect x="0" y="10" width="3" height="4" fill="var(--status-ink)"/>
        <rect x="5" y="7" width="3" height="7" fill="var(--status-ink)"/>
        <rect x="10" y="4" width="3" height="10" fill="var(--status-ink)"/>
        <rect x="15" y="0" width="3" height="14" fill="var(--status-ink)"/>
      </svg>
      <svg class="lock" width="14" height="16" viewBox="0 0 14 16" aria-label="Locked">
        <path d="M3.5 7V4.5a3.5 3.5 0 0 1 7 0V7" fill="none" stroke="var(--status-ink)" stroke-width="2"/>
        <rect x="1" y="7" width="12" height="9" rx="1.5" fill="var(--status-ink)"/>
      </svg>
      <svg class="battery" width="30" height="14" viewBox="0 0 30 14" aria-label="Battery">
        <rect x="0.75" y="0.75" width="25" height="12.5" rx="2" fill="none" stroke="var(--status-ink)" stroke-width="1.5"/>
        <rect x="3" y="3" width="20.5" height="8" fill="var(--status-ink)"/>
        <rect x="27" y="4.5" width="2.5" height="5" fill="var(--status-ink)"/>
      </svg>
    </header>

    <ul class="category-list">
      <li class="category category--business">
        <svg class="category__sheen" viewBox="0 0 484 122" preserveAspectRatio="none"><polygon points="300,0 484,0 484,122 250,122" fill="#ffffff" opacity="0.18"/></svg>
        <div class="category__icon" role="img" aria-label="Briefcase icon"></div>
        <span class="category__label">Business</span>
      </li>
      <li class="category category--education">
        <svg class="category__sheen" viewBox="0 0 484 122" preserveAspectRatio="none"><polygon points="300,0 484,0 484,122 250,122" fill="#ffffff" opacity="0.18"/></svg>
        <div class="category__icon" role="img" aria-label="Graduation cap icon"></div>
        <span class="category__label">Education</span>
      </li>
      <li class="category category--entertainment">
        <svg class="category__sheen" viewBox="0 0 484 122" preserveAspectRatio="none"><polygon points="300,0 484,0 484,122 250,122" fill="#ffffff" opacity="0.14"/></svg>
        <div class="category__icon" role="img" aria-label="Theatre masks icon"></div>
        <span class="category__label">Entertainment</span>
      </li>
      <li class="category category--finance">
        <div class="category__icon" role="img" aria-label="Piggy bank with coin icon"></div>
        <span class="category__label">Finance</span>
      </li>
      <li class="category category--games">
        <div class="category__icon" role="img" aria-label="Game controller buttons icon"></div>
        <span class="category__label">Games</span>
      </li>
    </ul>

    <footer class="unlock-panel">
      <div class="unlock-track">
        <div class="unlock-knob">
          <svg width="36" height="30" viewBox="0 0 36 30" aria-label="Arrow">
            <path d="M2 10h18V2l14 13-14 13v-8H2z" fill="var(--knob-ink)"/>
          </svg>
        </div>
        <span class="unlock-text">slide to unlock</span>
      </div>
    </footer>
  </main>
</body>
</html>
```